"Harrow Crest Builders" is a residential building company and needs a new business card design and may re

We would like a redesign based on the existing logo, and would like to see a new font as well. We are bespoke home builders who build sustainable energy efficient homes.

Industry/Entity Type

Construction

Contact Information for Business Card

Business card size 40mm x 90mm

Colors

Designer to choose colors to be used in the design.

```html
<!DOCTYPE html>
<html lang="en">
<head>
<meta charset="utf-8">
<title>Harrow Crest Builders – Business Card</title>
<link rel="stylesheet" href="https://fonts.googleapis.com/css2?family=Jura:wght@500;600&display=swap">
<style>
  :root {
    --backdrop: #8a6a48;
    --card: #ffffff;
    --ink: #111111;
    --accent: #a9c92f;
    --badge: #2c4a9a;
    --rule: #1a1a1a;
  }
  * { box-sizing: border-box; margin: 0; padding: 0; }
  html, body { width: 900px; height: 1200px; overflow: hidden; }
  body {
    background: var(--backdrop);
    font-family: "Jura", sans-serif;
    color: var(--ink);
    position: relative;
  }
  .card {
    position: absolute;
    left: 110px;
    width: 680px;
    height: 395px;
    background: var(--card);
    box-shadow: 0 4px 12px rgba(0,0,0,0.25);
  }
  .card--front { top: 167px; }
  .card--back { top: 627px; }

  /* Front */
  .brand {
    position: absolute;
    left: 78px;
    top: 128px;
    display: flex;
    align-items: center;
    gap: 143px;
  }
  .brand__square {
    width: 96px; height: 96px;
    flex: none;
    background: var(--accent);
  }
  .brand__name {
    font-weight: 600;
    color: var(--ink);
    line-height: 1.05;
    white-space: nowrap;
  }
  .brand__name-main { display: block; font-size: 46px; letter-spacing: 0.5px; }
  .brand__name-sub { display: block; font-size: 26px; letter-spacing: 1px; margin-top: 6px; }

  .front-web {
    position: absolute;
    left: 74px; right: 74px;
    top: 337px;
    display: flex;
    align-items: center;
    gap: 14px;
    font-size: 18px;
    font-weight: 600;
    letter-spacing: 0.5px;
    white-space: nowrap;
  }
  .front-web::before, .front-web::after {
    content: "";
    flex: 1;
    height: 1.5px;
    background: var(--rule);
  }

  /* Back */
  .back-mark {
    position: absolute;
    left: 66px; top: 98px;
    width: 120px; height: 120px;
    background: var(--accent);
  }
  .contact {
    position: absolute;
    left: 307px; top: 100px;
  }
  .contact__name {
    font-size: 23px;
    font-weight: 600;
    letter-spacing: 0.3px;
    margin-bottom: 12px;
  }
  .contact__list { list-style: none; }
  .contact__item {
    display: flex;
    align-items: center;
    gap: 12px;
    font-size: 17px;
    font-weight: 600;
    height: 28.5px;
    white-space: nowrap;
  }
  .contact__icon { width: 19px; height: 19px; flex: none; }

  .back-rule {
    position: absolute;
    left: 47px; right: 40px;
    top: 300px;
    height: 1.5px;
    background: var(--rule);
  }
  .legal {
    position: absolute;
    left: 46px; top: 320px;
    font-size: 15px;
    font-weight: 600;
    line-height: 24px;
    letter-spacing: 0.3px;
    white-space: nowrap;
  }
  .member-badge {
    position: absolute;
    left: 522px; top: 323px;
    width: 118px; height: 48px;
    background: var(--badge);
  }
</style>
</head>
<body>

<section class="card card--front">
  <div class="brand">
    <div class="brand__square"></div>
    <p class="brand__name">
      <span class="brand__name-main">Harrow Crest</span>
      <span class="brand__name-sub">Builders Pty Ltd</span>
    </p>
  </div>
  <p class="front-web">www.harrowcrestbuilders.com.au</p>
</section>

<section class="card card--back">
  <div class="back-mark"></div>

  <div class="contact">
    <h1 class="contact__name">Daniel Moretti</h1>
    <ul class="contact__list">
      <li class="contact__item">
        <svg class="contact__icon" viewBox="0 0 20 20" aria-hidden="true">
          <path d="M3 7c0-2 3-3 7-3s7 1 7 3v1.5h-3.5V7h-7v1.5H3z" fill="var(--accent)"/>
          <path d="M5 10h10l1.5 6h-13z" fill="var(--accent)"/>
        </svg>
        0491 570 318
      </li>
      <li class="contact__item">
        <svg class="contact__icon" viewBox="0 0 20 20" aria-hidden="true">
          <rect x="2" y="4" width="16" height="12" fill="var(--accent)"/>
          <path d="M2 4l8 7 8-7" fill="none" stroke="#fff" stroke-width="1.4"/>
        </svg>
        daniel@harrowcrestbuilders.com.au
      </li>
      <li class="contact__item">
        <svg class="contact__icon" viewBox="0 0 20 20" aria-hidden="true">
          <g fill="none" stroke="var(--accent)" stroke-width="1.6">
            <circle cx="10" cy="10" r="8"/>
            <ellipse cx="10" cy="10" rx="3.5" ry="8"/>
            <path d="M2 10h16M3.5 6h13M3.5 14h13"/>
          </g>
        </svg>
        www.harrowcrestbuilders.com.au
      </li>
    </ul>
  </div>

  <div class="back-rule"></div>

  <p class="legal">
    PO Box 2178 Eastgate LPO Kelmscott WA 6111<br>
    Registration 40583&nbsp; | &nbsp;ABN: 42 305 618 774
  </p>
  <div class="member-badge" role="img" aria-label="Industry association membership badge"></div>
</section>

</body>
</html>
```